Web Design Project

Brightwater Digital owns and operates a large number of editorial websites. These websites provides mostly consumers in the financial services space with information and price comparisons for a particular service.

Brightwater Digital, as the holding company for each of these sites, currently has no website. We need to build a website targeted towards potential partners for our websites. The idea being that when we start a conversation with a partner, they can view our site and obtain some basic information about who we are.

The structure of the site is to be very simple, containing only a brief description about who we are, our contact details and a list of some of our websites:
• CoverQuest.net.au
• AutoPolicyMatcher.com.au
• NestPolicyMatcher.com.au
• WellPolicyMatcher.com.au
• CoverQuestMatcher.com.au
• TripPolicyMatcher.com.au
• CritterPolicyMatcher.com.au
• CashAdvanceMatcher.com.au
• MobileCoolingUnit.com.au
• FixedSaverYields.com.au
• ThriftyHabits.com.au
• PurseGran.com.au
• TameThePlastic.com.au
• PurseMinder.com.au
• ThirdPartyClaimsCoverOzland.com.au
• Trade-Protect.com.au
• AutoPolicyProviders.com.au
• WellPolicyProviders.com.au
• NestPolicyOzland.com
• CoverQuestOzland.com
• WageShieldPolicyOzland.com
• WellPolicyOzland.com
• CritterPolicyOzland.com
• CashAdvancesOzland.com
• PlasticPaysOzland.com
• NestLendersOzland.com
• NestEggFunds.net.au

The design of the site should say 'Internet company', 'professional', 'fresh thinking'. The design should not look like a corporate site that you would see from any corporate services business with images of people in suits. We are ultimately an Internet business and there should be a unique feel to the site.

We are open to a suggestion of a colour pallet as the holding company does not have an established logo.

Some sites that we like are:

http://www.prismwork-studio.co.uk/#home
http://sample00.layoutvault.example/wt_48248/index.html
http://sample00.layoutvault.example/wordpress_46388/
http://mindvolt.example/
http://www.tandora.us/
http://www.kelvorabintu.example/
http://www.slickfrontpages.example/Corporate/design-ideas-detail.html?id=7916
http://trebla.example/
http://orvantek.example/

Reason: Hi all, Apologies, but I need to extend the timeline. One of our key stakeholders is away for the next week. There are a few good designs that we have received to date and there are some tweaks that we would like to see before making a final decision. Thank you to everyone that has submitted designs - Have a great new year. Derek

Reason: Sorry to have to delay the deadline on this, but we did not find anything in the designs really resonated with us. We will have a further think about the existing designs that have been submitted and how we can provide more specific feedback to the designers to make some modifications to the designs.

Target Market(s)

We are targeting insurance companies / brokers that we are talking to. The idea is that we show a professional face to them.

Industry/Entity Type

Financial

Requirements
Must have
• Home Page (possibly integrated with About us details)
Contact Us
Our Sites

```html
<!DOCTYPE html>
<html lang="en">
<head>
<meta charset="utf-8">
<title>Brightwater Digital</title>
<link rel="stylesheet" href="https://fonts.googleapis.com/css2?family=Open+Sans:wght@400;600;700&family=Arimo:wght@400;700&family=Crimson+Text:wght@700&display=swap">
<style>
:root{
  --blue-light:#6aa2f0;
  --blue-mid:#2f6fd6;
  --blue-dark:#124aa8;
  --heading:#1f57b8;
  --text:#333;
  --text-soft:#555;
  --rule:#c9d3e2;
  --panel:#f3f4f6;
  --line:#b9b9b9;
  --white:#fff;
}
*{box-sizing:border-box;margin:0;padding:0}
html,body{width:1117px;height:1200px;overflow:hidden;background:var(--white)}
body{position:relative;font-family:"Arimo",Arial,sans-serif;color:var(--text)}
.abs{position:absolute}

/* header */
.site-header{position:absolute;left:0;top:0;width:1117px;height:149px;
  background:linear-gradient(#5f99ec 0%,#3a78db 45%,#1a52b3 100%)}
.brand-mark{left:15px;top:36px;width:76px;height:76px;border:3px solid var(--white)}
.brand-name{left:103px;top:40px;font:700 37px/1 "Open Sans",sans-serif;color:var(--white);letter-spacing:.5px;text-transform:uppercase}
.phone-icon{left:934px;top:38px}
.phone-number{left:971px;top:44px;font:400 20px/1 "Open Sans",sans-serif;color:var(--white)}
.nav a{position:absolute;font:600 14px/1 "Open Sans",sans-serif;color:var(--white);text-decoration:none;white-space:nowrap}
.nav .sep{position:absolute;color:var(--white);font:400 14px/1 "Open Sans",sans-serif}

/* slider */
.slider-frame{left:11px;top:166px;width:1093px;height:382px;border:1px solid #ddd;background:var(--white)}
.slider{left:18px;top:173px;width:1079px;height:365px;border:1px solid #bbb;
  background:linear-gradient(90deg,#f4f5f6 0%,#eef0f2 40%,#e3e6ea 100%);overflow:hidden}
.slide-photo{position:absolute;left:487px;top:0;width:592px;height:365px;
  background:linear-gradient(100deg,rgba(238,240,243,0) 0%,#d9dde2 20%,#b9bec6 55%,#e8e9eb 100%)}
.slide-title{left:52px;top:48px;font:700 35px/1 "Crimson Text",serif;color:var(--heading);letter-spacing:.5px}
.slide-rule{left:21px;top:114px;width:470px;border-top:1px dotted #7aa0d8}
.slide-text{left:34px;top:142px;width:435px;font:400 13.4px/20px "Arimo",sans-serif;color:var(--text);letter-spacing:.2px}
.slide-text b{font-weight:700}
.btn-pill{display:flex;align-items:center;justify-content:center;color:var(--white);
  background:linear-gradient(#4d8ef0,#1a55c4);border-radius:12px;font-family:"Open Sans",sans-serif}
.slide-btn{left:312px;top:256px;width:153px;height:38px;font-size:18px;border-radius:12px}
.dots{left:1015px;top:341px;display:flex;gap:5px}
.dots span{width:13px;height:13px;border-radius:50%;background:#e7e9ec;border:1px solid #fff}
.dots span.on{background:#1e8fd9}
.slider-shadow{left:28px;top:546px;width:1060px;height:22px;
  background:radial-gradient(ellipse at 50% 0%,rgba(0,0,0,.35) 0%,rgba(0,0,0,0) 70%)}

/* partners */
.partners{left:36px;top:591px;width:291px;height:516px;border:1px solid #e3e3e3;border-radius:14px;
  background:linear-gradient(90deg,#f9f9f9,#eceef0)}
.partners-tab{left:28px;top:609px;width:196px;height:35px;border-radius:0 12px 12px 0;
  background:linear-gradient(#4f8ef0,#1b54c2)}
.partners-tab-icon{left:36px;top:611px}
.partners-title{left:75px;top:617px;font:400 18px/1 "Open Sans",sans-serif;color:var(--white)}
.partner-list{left:46px;top:659px;list-style:none;width:260px}
.partner-list li{position:relative;height:33.6px;padding-left:24px;font:400 13.3px/22px "Arimo",sans-serif;color:var(--text-soft);letter-spacing:.3px}
.partner-list li::before{content:"";position:absolute;left:1px;top:6px;width:10px;height:10px;background:#2c4fb3}
.partner-list li::after{content:"";position:absolute;left:1px;top:4px;width:0;height:0;border-left:4px solid #fff;border-top:3px solid transparent;border-bottom:3px solid transparent;margin:4px 0 0 3px}
.partner-list li + li{border-top:0}
.partner-list .rule{position:absolute;left:24px;right:0;top:-6px;border-top:1px dotted #b8b8b8}
.more-btn{left:293px;top:1076px}

/* about */
.section-title{font:700 27px/1 "Crimson Text",serif;color:var(--heading);letter-spacing:.5px}
.about-title{left:347px;top:591px}
.team-photo-frame{left:345px;top:636px;width:251px;height:159px;border:1px solid #ccc;background:var(--white)}
.team-photo{position:absolute;left:7px;top:7px;width:235px;height:143px;
  background:linear-gradient(135deg,#e9ecef,#b9c1ca 60%,#8e96a0)}
.about-text{left:614px;top:637px;width:468px;font:400 13.3px/20.2px "Arimo",sans-serif;color:var(--text);text-align:justify;letter-spacing:.2px}
.about-text b{font-weight:700}
.readmore{left:995px;top:772px;width:86px;height:22px;font-size:13px;border-radius:11px}

/* query + contact */
.info-box{left:343px;top:821px;width:743px;height:284px;border:1px solid #e2e2e2;
  background:linear-gradient(#fafafa,#ebebeb)}
.query-icon{left:354px;top:827px}
.query-title{left:395px;top:833px}
.field-label{position:absolute;right:673px;font:400 13.3px/1 "Arimo",sans-serif;color:var(--text-soft)}
.field{position:absolute;left:447px;width:194px;height:25px;background:var(--white);border:1px solid var(--line)}
.send-btn{left:557px;top:1069px;width:85px;height:20px;font-size:13px;border-radius:10px}
.divider{left:696px;top:864px;height:230px;border-left:1px dotted #bbb}
.contact-icon{left:703px;top:833px}
.contact-title{left:758px;top:833px}
.contact-lines{left:749px;top:885px;font:400 13.3px/33.6px "Arimo",sans-serif;color:var(--text)}
.contact-lines b{font-weight:700}

/* footer */
.site-footer{position:absolute;left:0;top:1128px;width:1117px;height:72px;
  background:linear-gradient(#5f99ec,#2d6bd4 55%,#1a52b3)}
.copyright{left:0;width:1117px;top:1174px;text-align:center;font:600 14px/1 "Open Sans",sans-serif;color:var(--white)}
</style>
</head>
<body>

<header class="site-header">
  <div class="abs brand-mark"></div>
  <div class="abs brand-name">Brightwater Digital</div>
  <svg class="abs phone-icon" width="30" height="38" viewBox="0 0 30 38" aria-hidden="true">
    <path d="M8 2 L14 2 L16 10 L12 13 C13 20 16 25 20 28 L24 25 L29 31 L25 36 C14 35 4 22 3 9 Z" fill="#0d1f3f"/>
  </svg>
  <div class="abs phone-number">0294713360</div>
  <nav class="nav">
    <a style="left:698px;top:113px">HOME</a><span class="sep" style="left:765px;top:113px">|</span>
    <a style="left:796px;top:113px">About Us</a><span class="sep" style="left:884px;top:113px">|</span>
    <a style="left:914px;top:113px">Projects</a><span class="sep" style="left:994px;top:113px">|</span>
    <a style="left:1025px;top:113px">Contact&nbsp; Us</a>
  </nav>
</header>

<div class="abs slider-frame"></div>
<section class="abs slider">
  <div class="slide-photo" role="img" aria-label="Smiling woman working on a laptop"></div>
  <h1 class="abs slide-title">Thrifty Habits</h1>
  <div class="abs slide-rule"></div>
  <p class="abs slide-text"><b>Lorem Ipsum is simply dummy</b> text of the printing and typesetting industry. Lorem Ipsum has been the industry's standard dummy text ever since the 1500s, when an unknown printer took a galley of type and scrambled it to make a type specimen book.</p>
  <div class="abs btn-pill slide-btn">View Details</div>
  <div class="abs dots"><span></span><span></span><span class="on"></span><span></span></div>
</section>
<div class="abs slider-shadow"></div>

<aside>
  <div class="abs partners"></div>
  <div class="abs partners-tab"></div>
  <svg class="abs partners-tab-icon" width="36" height="34" viewBox="0 0 36 34" aria-hidden="true">
    <circle cx="12" cy="9" r="7" fill="#f0c9a0"/><path d="M1 32 C1 20 23 20 23 32 Z" fill="#3a6fd0"/>
    <circle cx="25" cy="15" r="6" fill="#f0c9a0"/><path d="M15 34 C15 24 35 24 35 34 Z" fill="#d8503f"/>
  </svg>
  <h2 class="abs partners-title">Our Partners</h2>
  <ul class="abs partner-list">
    <li>CoverQuest.net.au</li>
    <li><span class="rule"></span>CoverQuestMatcher.com.au</li>
    <li><span class="rule"></span>AutoPolicyMatcher.com.au</li>
    <li><span class="rule"></span>AutoPolicyMatcher.com.au</li>
    <li><span class="rule"></span>NestPolicyMatcher.com.au</li>
    <li><span class="rule"></span>WellPolicyMatcher.com.au</li>
    <li><span class="rule"></span>WellPolicyMatcher.com.au</li>
    <li><span class="rule"></span>CoverQuestMatcher.com.au</li>
    <li><span class="rule"></span>NestPolicyMatcher.com.au</li>
    <li><span class="rule"></span>NestPolicyMatcher.com.au</li>
    <li><span class="rule"></span>WellPolicyMatcher.com.au</li>
    <li><span class="rule"></span>CoverQuestMatcher.com.au</li>
    <li><span class="rule"></span>ThriftyHabits.com.au</li>
  </ul>
  <svg class="abs more-btn" width="24" height="24" viewBox="0 0 24 24" aria-hidden="true">
    <circle cx="12" cy="12" r="11" fill="#1f5fc8" stroke="#a9c4ef" stroke-width="1.5"/>
    <path d="M12 6 V18 M6 12 H18" stroke="#fff" stroke-width="3"/>
  </svg>
</aside>

<section>
  <h2 class="abs section-title about-title">About Us</h2>
  <div class="abs team-photo-frame"><div class="team-photo" role="img" aria-label="Team of four colleagues gathered around a laptop"></div></div>
  <p class="abs about-text"><b>Brightwater Digital is an Australian-based internet marketing company. We specialise</b> in attracting customers from our directory of more than 100 sites to our network of trusted partners. Our skill lies in generating targeted traffic to our range of websites and identifying the right partners for each of the sites, ensuring that the visitors to our sites get what they are looking for. Our skill lies in generating targeted traffic to our range of websites</p>
  <div class="abs btn-pill readmore">Readmore</div>
</section>

<section>
  <div class="abs info-box"></div>
  <svg class="abs query-icon" width="30" height="44" viewBox="0 0 30 44" aria-hidden="true">
    <path d="M5 12 C5 3 25 1 25 12 C25 20 15 20 15 29" fill="none" stroke="#2a56a8" stroke-width="5" stroke-linecap="round"/>
    <circle cx="15" cy="39" r="3.5" fill="#2a56a8"/>
  </svg>
  <h2 class="abs section-title query-title">Send Query</h2>
  <span class="field-label" style="top:890px">Username :</span><span class="field" style="top:884px"></span>
  <span class="field-label" style="top:923px">Email :</span><span class="field" style="top:917px"></span>
  <span class="field-label" style="top:957px">Phone :</span><span class="field" style="top:951px"></span>
  <span class="field-label" style="top:991px">Comments :</span><span class="field" style="top:985px;height:69px"></span>
  <div class="abs btn-pill send-btn">Send</div>

  <div class="abs divider"></div>

  <svg class="abs contact-icon" width="42" height="32" viewBox="0 0 42 32" aria-hidden="true">
    <path d="M3 10 C3 3 39 3 39 10 L33 13 L29 9 L13 9 L9 13 Z" fill="#2a6cc9"/>
    <path d="M12 12 L30 12 L37 29 L5 29 Z" fill="#3f86dc"/>
    <circle cx="21" cy="20" r="5" fill="#cfe1f7"/>
  </svg>
  <h2 class="abs section-title contact-title">Contact Us</h2>
  <div class="abs contact-lines">
    <b>Brightwater Digital Pty Ltd</b><br>
    Suite 412<br>
    18 Harbourview Lane<br>
    Coral Bay NSW&nbsp;&nbsp; 2199<br>
    <b>Tel:</b> 02 9471 3360<br>
    <b>Email:</b> info@brightwaterdigital.example
  </div>
</section>

<footer class="site-footer">
  <nav class="nav">
    <a style="left:388px;top:14px">HOME</a><span class="sep" style="left:455px;top:14px">|</span>
    <a style="left:487px;top:14px">About Us</a><span class="sep" style="left:573px;top:14px">|</span>
    <a style="left:604px;top:14px">Projects</a><span class="sep" style="left:683px;top:14px">|</span>
    <a style="left:716px;top:14px">Contact&nbsp; Us</a>
  </nav>
</footer>
<div class="abs copyright">Copyright Brightwater Digital @ 2011-12.</div>

</body>
</html>
```